I need a flyer designed for a marine service company. Our company specializes in boat engine diagnostic/repair, engine service, electronic installation and repairs, bottom paint, detailing, winterization and shrink wrapping. We would like to see designs that incorporate our color scheme of deep blue, blueish gray and black (please see attached photo)

Target Market(s)

Boat owners

Industry/Entity Type

Marine

Logo Text

Kelpridge Harbor Services

Requirements
Must have
• Company logo
Nice to have
• List the services we provide.

```html
<!DOCTYPE html>
<html lang="en">
<head>
<meta charset="utf-8">
<title>Kelpridge Harbor Services – Flyer</title>
<link href="https://fonts.googleapis.com/css2?family=Poppins:wght@400;500;600;700&display=swap" rel="stylesheet">
<style>
  :root{
    --navy:#132f5a;
    --navy-deep:#0f2749;
    --sea:#1d5a92;
    --sea-light:#3f7fb8;
    --sky:#e6eefa;
    --mist:#b9cbe3;
    --white:#ffffff;
    --stage:#cbcbcb;
  }
  *{margin:0;padding:0;box-sizing:border-box}
  html,body{width:1200px;height:1200px;overflow:hidden;background:var(--stage);font-family:"Poppins",sans-serif}
  .flyer{
    position:absolute;left:50px;top:211px;
    width:1456px;height:1028px;
    transform:scale(0.7555);transform-origin:0 0;
    overflow:hidden;background:var(--sky);
  }
  .flyer__art{position:absolute;inset:0;width:1456px;height:1028px}
  .highlights{position:absolute;left:78px;top:26px;list-style:none}
  .highlights li{display:flex;align-items:center;height:67px;color:var(--navy);font-weight:600;font-size:40px;letter-spacing:-0.3px}
  .highlights .icon{width:52px;height:52px;margin-right:14px;flex:none}
  .services-title{position:absolute;left:78px;top:390px;color:var(--white);font-weight:600;font-size:70px;line-height:1;letter-spacing:-0.5px}
  .services-rule{position:absolute;left:67px;top:473px;width:560px;height:2px;background:linear-gradient(90deg,var(--white),rgba(255,255,255,.2))}
  .services{position:absolute;list-style:none;color:var(--white);font-size:22px;font-weight:400}
  .services li{position:absolute;display:flex;align-items:flex-start;white-space:nowrap;line-height:28px}
  .services .tick{width:27px;height:27px;margin-right:20px;flex:none}
  .logo-badge{position:absolute;left:1110px;top:27px;width:294px;height:294px;border-radius:50%;background:var(--white);display:flex;flex-direction:column;align-items:center;justify-content:center;text-align:center;color:var(--navy);font-weight:600;font-size:31px;line-height:1.25}
  .contact{position:absolute;left:65px;top:940px;width:1330px;height:60px;display:flex;align-items:center;color:var(--white)}
  .contact__cta{font-size:29px;font-weight:500;letter-spacing:-0.3px;margin-right:26px}
  .contact__icon{width:42px;height:42px;flex:none;margin-right:10px}
  .contact__phone{font-size:36px;font-weight:700;letter-spacing:-0.3px}
  .contact__divider{width:3px;height:46px;background:var(--white);margin:0 38px}
  .contact__email{font-size:28px;font-weight:500;margin-left:8px}
</style>
</head>
<body>
<div class="flyer">
  <svg class="flyer__art" viewBox="0 0 1456 1028" xmlns="http://www.w3.org/2000/svg">
    <defs>
      <linearGradient id="skyWater" x1="0" y1="0" x2="0" y2="1">
        <stop offset="0" stop-color="#c7d6ec"/>
        <stop offset="0.6" stop-color="#eef3fb"/>
        <stop offset="1" stop-color="#ffffff"/>
      </linearGradient>
      <radialGradient id="seaBoat" cx="0.75" cy="0.45" r="0.7">
        <stop offset="0" stop-color="#dfe8f2"/>
        <stop offset="0.3" stop-color="#7fa6cc"/>
        <stop offset="0.6" stop-color="#2a67a0"/>
        <stop offset="1" stop-color="#174a80"/>
      </radialGradient>
      <linearGradient id="partsPhoto" x1="0" y1="0" x2="1" y2="1">
        <stop offset="0" stop-color="#e9ece8"/><stop offset="1" stop-color="#b8b6a8"/>
      </linearGradient>
      <linearGradient id="trailerPhoto" x1="0" y1="0" x2="0" y2="1">
        <stop offset="0" stop-color="#9fb1c8"/><stop offset="0.5" stop-color="#e8e8e6"/><stop offset="1" stop-color="#3b3b3d"/>
      </linearGradient>
      <linearGradient id="workPhoto" x1="0" y1="0" x2="1" y2="1">
        <stop offset="0" stop-color="#6e6a66"/><stop offset="0.5" stop-color="#d9d9d6"/><stop offset="1" stop-color="#8a8a88"/>
      </linearGradient>
    </defs>
    <rect width="1456" height="1028" fill="url(#skyWater)" role="img" aria-label="Calm open water seen from above"/>
    <path d="M0,440 C300,300 700,230 1000,232 C1200,234 1380,290 1456,345 L1456,595 C1200,730 900,830 620,832 C400,830 150,760 0,705 Z"
          fill="url(#seaBoat)" role="img" aria-label="White motor yacht speeding across deep blue sea with a foaming wake"/>
    <path d="M0,440 C300,300 700,230 1000,232 C1200,234 1380,290 1456,345" fill="none" stroke="var(--navy)" stroke-width="7"/>
    <path d="M0,720 C150,775 400,845 620,847 C900,845 1200,745 1456,610 L1456,1028 L0,1028 Z" fill="var(--navy)"/>
    <circle cx="242" cy="785" r="110" fill="url(#partsPhoto)" stroke="#fff" stroke-width="5" role="img" aria-label="Disassembled carburetor parts laid out on a bench"/>
    <circle cx="630" cy="767" r="135" fill="url(#trailerPhoto)" stroke="#fff" stroke-width="5" role="img" aria-label="Bowrider boat resting on a trailer at the marina"/>
    <circle cx="1062" cy="710" r="160" fill="url(#workPhoto)" stroke="#fff" stroke-width="5" role="img" aria-label="Technician working inside a boat hull in the yard"/>
  </svg>

  <ul class="highlights">
    <li><svg class="icon" viewBox="0 0 52 52"><circle cx="26" cy="26" r="24" fill="none" stroke="var(--navy)" stroke-width="2"/><path d="M16 36 L36 16 M20 28 l4 4 M24 24 l4 4 M28 20 l4 4" stroke="var(--navy)" stroke-width="2.5" fill="none" stroke-linecap="round"/></svg>INBOARD MOTORS</li>
    <li><svg class="icon" viewBox="0 0 52 52"><circle cx="26" cy="26" r="24" fill="none" stroke="var(--navy)" stroke-width="2"/><circle cx="26" cy="26" r="3" fill="var(--navy)"/><path d="M26 23 C20 14 32 12 28 23 M29 27 C38 26 34 37 26 29 M23 27 C16 34 12 22 23 25" fill="none" stroke="var(--navy)" stroke-width="2"/></svg>OUTBOARD MOTORS</li>
    <li><svg class="icon" viewBox="0 0 52 52"><circle cx="26" cy="26" r="24" fill="none" stroke="var(--navy)" stroke-width="2"/><path d="M12 29 H40 L36 35 H16 Z M18 29 V24 H32 L35 29 M22 24 V20 H28 V24" fill="none" stroke="var(--navy)" stroke-width="2"/></svg>ALL MAKES &amp; MODELS</li>
    <li><svg class="icon" viewBox="0 0 52 52"><circle cx="26" cy="26" r="24" fill="none" stroke="var(--navy)" stroke-width="2"/><path d="M12 32 H38 L41 28 H28 L24 22 H19 L18 28 H12 Z" fill="none" stroke="var(--navy)" stroke-width="2"/></svg>JETSKIS</li>
  </ul>

  <div class="logo-badge"><span>Kelpridge</span><span>Harbor Services</span></div>

  <h2 class="services-title">Our Services</h2>
  <div class="services-rule"></div>
  <ul class="services">
    <li style="left:78px;top:500px"><svg class="tick" viewBox="0 0 27 27"><rect x="2" y="4" width="21" height="21" rx="3" fill="none" stroke="#fff" stroke-width="2.5"/><path d="M7 14 l5 5 L25 4" fill="none" stroke="#fff" stroke-width="3" stroke-linecap="round"/></svg>Diagnostic/repair</li>
    <li style="left:78px;top:546px"><svg class="tick" viewBox="0 0 27 27"><rect x="2" y="4" width="21" height="21" rx="3" fill="none" stroke="#fff" stroke-width="2.5"/><path d="M7 14 l5 5 L25 4" fill="none" stroke="#fff" stroke-width="3" stroke-linecap="round"/></svg>Bottom paint</li>
    <li style="left:78px;top:597px"><svg class="tick" viewBox="0 0 27 27" style="margin-right:14px"><rect x="2" y="4" width="21" height="21" rx="3" fill="none" stroke="#fff" stroke-width="2.5"/><path d="M7 14 l5 5 L25 4" fill="none" stroke="#fff" stroke-width="3" stroke-linecap="round"/></svg>Detailing</li>
    <li style="left:340px;top:498px"><svg class="tick" viewBox="0 0 27 27" style="margin-right:10px"><rect x="2" y="4" width="21" height="21" rx="3" fill="none" stroke="#fff" stroke-width="2.5"/><path d="M7 14 l5 5 L25 4" fill="none" stroke="#fff" stroke-width="3" stroke-linecap="round"/></svg>Engine service</li>
    <li style="left:340px;top:546px"><svg class="tick" viewBox="0 0 27 27" style="margin-right:10px"><rect x="2" y="4" width="21" height="21" rx="3" fill="none" stroke="#fff" stroke-width="2.5"/><path d="M7 14 l5 5 L25 4" fill="none" stroke="#fff" stroke-width="3" stroke-linecap="round"/></svg>Shrink wrapping</li>
    <li style="left:340px;top:596px"><svg class="tick" viewBox="0 0 27 27" style="margin-right:19px"><rect x="2" y="4" width="21" height="21" rx="3" fill="none" stroke="#fff" stroke-width="2.5"/><path d="M7 14 l5 5 L25 4" fill="none" stroke="#fff" stroke-width="3" stroke-linecap="round"/></svg><span>Electronic installation<br>and repairs</span></li>
  </ul>

  <div class="contact">
    <span class="contact__cta">CALL FOR A QUOTE TODAY</span>
    <svg class="contact__icon" viewBox="0 0 42 42"><circle cx="21" cy="21" r="20" fill="#fff"/><path d="M14 11 l5 5 -3 3 c2 4 4 6 7 7 l3 -3 5 5 -3 3 c-8 0 -17 -9 -17 -17 Z" fill="var(--navy)"/></svg>
    <span class="contact__phone">(555) 318-4062</span>
    <span class="contact__divider"></span>
    <svg class="contact__icon" viewBox="0 0 42 42"><circle cx="21" cy="21" r="20" fill="#fff"/><rect x="11" y="14" width="20" height="14" rx="1.5" fill="none" stroke="var(--navy)" stroke-width="2"/><path d="M11 15 L21 23 L31 15" fill="none" stroke="var(--navy)" stroke-width="2"/></svg>
    <span class="contact__email">hello@kelpridgeharbor.com</span>
  </div>
</div>
</body>
</html>
```